Copperfield Ridge Dental business card

Business card would have following info:

Harold T. Quenneville, DMD, FAGD
General Dentist
email: office@copperfieldridgedental.com
phone: 413-867-3094
fax: 413-867-3094
website: copperfieldridgedental.com

second side would have lines for:

appointment date
appointment time

```html
<!DOCTYPE html>
<html lang="en">
<head>
<meta charset="utf-8">
<title>Copperfield Ridge Dental – Business Card</title>
<link rel="stylesheet" href="https://fonts.googleapis.com/css2?family=Fira+Sans:wght@400;600;700&family=Ubuntu:wght@400&family=Roboto:wght@400;700&display=swap">
<style>
  :root {
    --navy: #07507f;
    --orange: #ef8f22;
    --white: #ffffff;
    --ink: #2a2a2a;
    --backdrop: #3a3a3a;
  }
  * { box-sizing: border-box; margin: 0; padding: 0; }
  html, body { width: 1200px; height: 1059px; overflow: hidden; }
  body { background: var(--backdrop); position: relative; font-family: "Ubuntu", sans-serif; }

  .card {
    position: absolute;
    width: 688px; height: 392px;
    border-radius: 20px;
    overflow: hidden;
  }
  .card--front { left: 256px; top: 100px; background: var(--white); }
  .card--back  { left: 256px; top: 537px; background: var(--navy); }

  .band { position: absolute; left: 0; width: 688px; height: 15px; display: block; }
  .band--top { top: 0; }
  .band--bottom { bottom: 0; }

  .practice-name {
    position: absolute; left: 0; right: 0;
    text-align: center;
    font-family: "Fira Sans", sans-serif;
    font-weight: 600;
    letter-spacing: 0.5px;
  }
  .card--front .practice-name { top: 104px; font-size: 40px; color: var(--navy); }
  .card--back .practice-name { top: 96px; font-size: 48px; color: var(--white); }

  .dentist {
    position: absolute; right: 370px; top: 233px;
    text-align: right;
    font-family: "Fira Sans", sans-serif;
  }
  .dentist__name { font-size: 21px; font-weight: 600; color: var(--navy); line-height: 28px; white-space: nowrap; }
  .dentist__credentials { font-size: 21px; font-weight: 600; color: var(--orange); line-height: 28px; }
  .dentist__role { font-size: 14px; color: var(--ink); line-height: 22px; letter-spacing: 0.5px; font-family: "Ubuntu", sans-serif; }

  .divider { position: absolute; left: 345px; top: 225px; width: 2px; height: 94px; background: var(--navy); }

  .contact { position: absolute; left: 364px; top: 220px; list-style: none; }
  .contact__item {
    display: flex; align-items: center;
    height: 26.5px;
    font-size: 16px; color: var(--ink);
  }
  .contact__icon { width: 13px; height: 13px; margin-right: 10px; flex: none; }

  .appointment__heading {
    position: absolute; left: 0; right: 0; top: 225px;
    text-align: center;
    font-family: "Roboto", sans-serif; font-weight: 700;
    font-size: 19px; color: var(--orange);
  }
  .appointment__rule { position: absolute; left: 242px; top: 269px; width: 206px; height: 1px; background: var(--orange); }

  .appointment__fields {
    position: absolute; left: 31px; top: 289px; width: 630px;
    display: flex; align-items: baseline;
    font-family: "Roboto", sans-serif; font-size: 16px; color: var(--white);
  }
  .field-line { border-bottom: 1px dashed var(--white); height: 14px; margin: 0 6px; }
  .field-line--date { width: 274px; }
  .field-line--time { width: 200px; }

  .appointment__days {
    position: absolute; left: 0; top: 331px; width: 688px; height: 22px;
    font-family: "Roboto", sans-serif; font-size: 16px; color: var(--white);
  }
  .day { position: absolute; display: flex; align-items: center; }
  .day__box { width: 11px; height: 11px; border: 2px solid var(--orange); margin-right: 7px; }
</style>
</head>
<body>

<section class="card card--front" aria-label="Card front">
  <svg class="band band--top" viewBox="0 0 688 15" preserveAspectRatio="none" aria-hidden="true">
    <polygon points="0,0 343,0 331,15 0,15" fill="var(--navy)"/>
    <polygon points="352,0 688,0 688,15 340,15" fill="var(--orange)"/>
  </svg>

  <h1 class="practice-name">COPPERFIELD RIDGE DENTAL</h1>

  <div class="dentist">
    <p class="dentist__name">HAROLD T. QUENNEVILLE</p>
    <p class="dentist__credentials">DMD, FAGD</p>
    <p class="dentist__role">GENERAL DENTIST</p>
  </div>

  <div class="divider"></div>

  <ul class="contact">
    <li class="contact__item">
      <svg class="contact__icon" viewBox="0 0 16 16" aria-hidden="true"><path d="M3 1l3 3-1.5 2a9 9 0 005.5 5.5L12 10l3 3-2 2C7 15 1 9 1 3z" fill="var(--orange)"/></svg>
      413-867-3094
    </li>
    <li class="contact__item">
      <svg class="contact__icon" viewBox="0 0 16 16" aria-hidden="true"><rect x="4" y="1" width="8" height="4" fill="var(--orange)"/><rect x="1" y="6" width="14" height="6" rx="1" fill="var(--orange)"/><rect x="4" y="10" width="8" height="5" fill="var(--orange)" stroke="var(--white)" stroke-width="1"/></svg>
      413-867-3094
    </li>
    <li class="contact__item">
      <svg class="contact__icon" viewBox="0 0 16 16" aria-hidden="true"><rect x="1" y="3" width="14" height="10" fill="var(--orange)"/><path d="M1 3l7 6 7-6M1 13l5-5M15 13l-5-5" stroke="var(--white)" stroke-width="1.2" fill="none"/></svg>
      office@copperfieldridgedental.com
    </li>
    <li class="contact__item">
      <svg class="contact__icon" viewBox="0 0 16 16" aria-hidden="true"><circle cx="8" cy="8" r="7" fill="var(--orange)"/><path d="M4 4c2 1 3 3 2 5M10 9c2 0 3 2 2 4" stroke="var(--white)" stroke-width="1.5" fill="none"/></svg>
      www.copperfieldridgedental.com
    </li>
  </ul>

  <svg class="band band--bottom" viewBox="0 0 688 15" preserveAspectRatio="none" aria-hidden="true">
    <polygon points="0,0 343,0 331,15 0,15" fill="var(--navy)"/>
    <polygon points="352,0 688,0 688,15 340,15" fill="var(--orange)"/>
  </svg>
</section>

<section class="card card--back" aria-label="Card back">
  <svg class="band band--top" viewBox="0 0 688 15" preserveAspectRatio="none" aria-hidden="true">
    <polygon points="0,0 343,0 331,15 0,15" fill="var(--white)"/>
    <polygon points="352,0 688,0 688,15 340,15" fill="var(--orange)"/>
  </svg>

  <h2 class="practice-name">COPPERFIELD RIDGE DENTAL</h2>

  <h3 class="appointment__heading">YOUR APPOINTMENT</h3>
  <div class="appointment__rule"></div>

  <div class="appointment__fields">
    <span>Date</span><span class="field-line field-line--date"></span>
    <span>Time</span><span class="field-line field-line--time"></span>
    <span>am/pm</span>
  </div>

  <div class="appointment__days">
    <span class="day" style="left:31px"><span class="day__box"></span>Mon</span>
    <span class="day" style="left:146px"><span class="day__box"></span>Tuse</span>
    <span class="day" style="left:265px"><span class="day__box"></span>Wed</span>
    <span class="day" style="left:381px"><span class="day__box"></span>Thur</span>
    <span class="day" style="left:505px"><span class="day__box"></span>Fri</span>
    <span class="day" style="left:619px"><span class="day__box"></span>Sat</span>
  </div>

  <svg class="band band--bottom" viewBox="0 0 688 15" preserveAspectRatio="none" aria-hidden="true">
    <polygon points="0,0 343,0 331,15 0,15" fill="var(--white)"/>
    <polygon points="352,0 688,0 688,15 340,15" fill="var(--orange)"/>
  </svg>
</section>

</body>
</html>
```